Packaging Design Project

We need a packaging design for a portable solar charger and 3-way cable.
The package style that is added in the pictures is preferred but we are open to suggestions.
I also added the cut line for the paper with fold lines

Industry/Entity Type

Solar

```html
<!DOCTYPE html>
<html lang="en">
<head>
<meta charset="utf-8">
<title>Solar Charger – Packaging Dieline</title>
<link href="https://fonts.googleapis.com/css2?family=Syncopate:wght@400;700&display=swap" rel="stylesheet">
<style>
  :root {
    --page: #ffffff;
    --band-top: #0c0c0f;
    --band-mid: #1e1f24;
    --band-low: #2a2c33;
    --footer-band: #3a3f4e;
    --accent-blue: #0d5ea8;
    --accent-blue-edge: #2b8fe0;
    --text: #e8e8ea;
    --text-dim: #b9bcc4;
    --cut-line: #e0822a;
    --fold-line: #4a4b52;
    --flap: #111114;
  }
  * { margin: 0; padding: 0; box-sizing: border-box; }
  html, body { width: 1200px; height: 527px; overflow: hidden; background: var(--page); }
  .canvas {
    position: relative; width: 1200px; height: 527px; overflow: hidden;
    font-family: "Syncopate", "Arial", sans-serif; color: var(--text);
  }
  .sleeve {
    position: absolute; left: 0; top: 91px; width: 777px; height: 343px;
    background: linear-gradient(180deg, var(--band-top) 0%, var(--band-mid) 55%, var(--band-low) 100%);
  }
  .sleeve__footer {
    position: absolute; left: 0; top: 283px; width: 777px; height: 60px;
    background: radial-gradient(ellipse at 60% 60%, #4a5266 0%, var(--footer-band) 35%, #1b1c22 100%);
  }
  .front-panel__stripe {
    position: absolute; left: 65px; top: 91px; width: 157px; height: 343px;
    background: linear-gradient(180deg, rgba(20,110,200,.55) 0%, rgba(13,94,168,.35) 50%, rgba(13,94,168,.75) 100%);
    border: 1px solid var(--accent-blue-edge);
    box-shadow: 0 4px 10px rgba(0,0,0,.25);
  }
  .wave {
    position: absolute;
  }
  .wave--front {
    left: 0; top: 141px; width: 347px; height: 77px;
    background: linear-gradient(180deg, rgba(30,120,220,0) 0%, rgba(40,140,235,.65) 45%, rgba(20,90,180,.35) 70%, rgba(30,120,220,0) 100%);
  }
  .wave--back {
    left: 392px; top: 153px; width: 339px; height: 49px;
    background: linear-gradient(180deg, rgba(120,130,150,0) 0%, rgba(120,130,150,.35) 50%, rgba(120,130,150,0) 100%);
  }
  .product-shot {
    position: absolute; left: 85px; top: 216px; width: 97px; height: 147px;
    border-radius: 8px;
    background: linear-gradient(135deg, #3a3d44 0%, #15161a 55%, #8c8f96 100%);
  }
  .flip { position: absolute; transform: rotate(180deg); }
  .tagline { left: 113px; top: 112px; width: 210px; font-size: 6.4px; line-height: 10px; letter-spacing: .5px; text-align: left; }
  .features { left: 228px; top: 286px; width: 100px; font-size: 6.4px; line-height: 10.5px; letter-spacing: .4px; text-align: right; color: var(--text-dim); }
  .hub-note { left: 228px; top: 362px; width: 90px; font-size: 6.4px; letter-spacing: .5px; text-align: right; }
  .title {
    left: 70px; top: 381px; width: 260px; font-size: 17px; letter-spacing: 1.5px; text-align: center; font-weight: 400;
  }
  .specs { left: 408px; top: 232px; width: 258px; font-size: 7.6px; line-height: 13.6px; letter-spacing: .8px; text-align: right; }
  .origin { left: 630px; top: 114px; width: 80px; font-size: 5.6px; letter-spacing: .4px; text-align: center; color: var(--text-dim); }
  .cert-marks { position: absolute; left: 403px; top: 113px; width: 100px; height: 12px; display: flex; gap: 10px; align-items: center; justify-content: space-between; }
  .cert-mark { width: 10px; height: 10px; background: var(--text-dim); border-radius: 2px; }
  .cert-mark--round { border-radius: 50%; }
  .cert-mark--wide { width: 16px; background: #4c8a4a; }
  .side-title {
    position: absolute; font-size: 10px; letter-spacing: 1.6px; white-space: nowrap;
    transform: translate(-50%, -50%) rotate(-90deg);
  }
  .side-title--spine { left: 367px; top: 303px; }
  .side-title--end { left: 755px; top: 303px; }
  .tray { position: absolute; left: 0; top: 0; width: 1200px; height: 527px; }
</style>
</head>
<body>
<main class="canvas">
  <section class="sleeve" aria-label="Sleeve wrap"></section>
  <div class="sleeve__footer"></div>

  <div class="wave wave--front" role="img" aria-label="Flowing blue light wave decoration"></div>
  <div class="wave wave--back" role="img" aria-label="Soft grey light wave decoration"></div>
  <div class="front-panel__stripe"></div>
  <div class="product-shot" role="img" aria-label="Photo of the solar charger with dock connector"></div>

  <p class="flip tagline">Portable solar charger for an NovaPhone<br>with 3-way USB cable</p>
  <p class="flip features">Portable 2200 mAh<br>Solar battery pack<br>Works with all micro<br>USB and NovaDevices</p>
  <p class="flip hub-note">with USB hub</p>
  <h1 class="flip title">Solar Charger</h1>

  <p class="flip specs">
    Capacity: 2200 mAh<br>
    Input 5V-0.5A<br>
    Output 5V-0.5A<br>
    Charging time 3 hours<br>
    Standby time up to 230 hours<br>
    Internet/Talktime up to 4 hours on 3G<br>
    Audio play up to 18 hours<br>
    Video play up to 5 hours
  </p>

  <div class="cert-marks" aria-label="Certification marks">
    <span class="cert-mark cert-mark--round"></span>
    <span class="cert-mark cert-mark--wide"></span>
    <span class="cert-mark"></span>
    <span class="cert-mark"></span>
  </div>
  <p class="flip origin">Made in China</p>

  <p class="side-title side-title--spine">Solar Charger</p>

  <svg class="tray" viewBox="0 0 1200 527" aria-label="Tray dieline">
    <defs>
      <linearGradient id="trayFill" x1="0" y1="0" x2="1" y2="1">
        <stop offset="0" stop-color="#0d0d10"/>
        <stop offset="0.5" stop-color="#24252b"/>
        <stop offset="1" stop-color="#111114"/>
      </linearGradient>
    </defs>
    <rect x="732" y="91" width="45" height="343" fill="#1c1d22"/>
    <rect x="777" y="44" width="342" height="47" fill="var(--flap)"/>
    <rect x="777" y="91" width="342" height="343" fill="url(#trayFill)"/>
    <rect x="777" y="434" width="342" height="42" fill="#24252b"/>
    <rect x="1119" y="91" width="49" height="343" fill="#141417"/>

    <g stroke="var(--fold-line)" stroke-width="0.8" fill="none">
      <rect x="833" y="148" width="230" height="229"/>
      <rect x="868" y="182" width="160" height="160"/>
      <line x1="777" y1="91" x2="1119" y2="434"/>
      <line x1="1119" y1="91" x2="777" y2="434"/>
    </g>

    <g stroke="var(--cut-line)" stroke-width="1" fill="none">
      <polyline points="777,44 840,0 1058,0 1119,44"/>
      <rect x="732" y="91" width="436" height="343"/>
      <line x1="777" y1="44" x2="777" y2="476"/>
      <line x1="1119" y1="44" x2="1119" y2="476"/>
      <line x1="777" y1="44" x2="1119" y2="44"/>
      <line x1="777" y1="476" x2="1119" y2="476"/>
      <polyline points="777,476 840,527 1058,527 1119,476"/>
      <polyline points="777,44 752,54 732,91"/>
      <polyline points="777,476 752,466 732,434"/>
      <polyline points="1119,44 1148,60 1168,91"/>
      <polyline points="1119,476 1148,462 1168,434"/>
      <polyline points="1168,91 1200,130"/>
      <polyline points="1168,434 1200,395"/>
    </g>
    <g stroke="var(--fold-line)" stroke-width="0.8">
      <line x1="752" y1="70" x2="777" y2="91"/>
      <line x1="1145" y1="70" x2="1119" y2="91"/>
      <line x1="752" y1="455" x2="777" y2="434"/>
      <line x1="1145" y1="455" x2="1119" y2="434"/>
    </g>
  </svg>

  <p class="side-title side-title--end">Solar Charger</p>
</main>
</body>
</html>
```